K.T.L Electrical Services Pty Ltd

Electrical contracting business. I have a base for the design which i like. The contact number needs to be changed to 0491736250 and the O made more solid and level with the rest of the letters. If you have any other ideas of what would make it better I'm happy to see them.

The back side to be written as dot points with the following:
- Residential & Commercial
- Maintenance
- PV & Battery servicing
- EV Chargers

```html
<!DOCTYPE html>
<html lang="en">
<head>
<meta charset="utf-8">
<title>K.T.L Electrical Services – Business Card</title>
<link href="https://fonts.googleapis.com/css2?family=Poppins:wght@400;500;600&family=Montserrat:wght@500&display=swap" rel="stylesheet">
<style>
  :root {
    --bg: #b3b3b3;
    --card: #070605;
    --teal: #8fb0b1;
    --orange: #dfa070;
    --grey: #a3a3a3;
  }
  * { margin: 0; padding: 0; box-sizing: border-box; }
  html, body { width: 1093px; height: 1200px; overflow: hidden; }
  body {
    background: var(--bg);
    font-family: "Poppins", sans-serif;
    position: relative;
  }
  .card {
    position: absolute;
    left: 265px;
    width: 580px;
    height: 360px;
    background: var(--card);
    border-radius: 26px;
    overflow: hidden;
  }
  .card--front { top: 226px; }
  .card--back { top: 621px; }

  .holder { position: absolute; left: 23px; top: 40px; }
  .holder__name {
    color: var(--teal);
    font-weight: 600;
    font-size: 20px;
    line-height: 22px;
    letter-spacing: 0.2px;
  }
  .holder__role { color: var(--grey); font-size: 16.5px; line-height: 20px; }

  .contact { position: absolute; left: 23px; top: 148px; list-style: none; }
  .contact li {
    display: flex; align-items: center; gap: 7px;
    color: var(--grey); font-size: 17.5px; line-height: 21px;
  }
  .contact li svg { width: 15px; height: 15px; flex: none; }
  .contact .contact__phone { color: var(--orange); }

  .address {
    position: absolute; left: 23px; top: 280px;
    color: var(--grey); font-size: 17.5px; line-height: 21px; font-style: normal;
  }

  .feature-art {
    position: absolute; left: 284px; top: 6px;
    width: 226px; height: 354px;
    border-radius: 22px 22px 0 0;
    background: linear-gradient(180deg, rgba(143,176,177,0.22), rgba(223,160,112,0.16) 55%, rgba(143,176,177,0.18));
  }

  .brand {
    position: absolute; left: 0; right: 0; top: 88px;
    text-align: center; color: var(--teal);
    font-family: "Montserrat", sans-serif; font-weight: 500;
  }
  .brand__name { font-size: 102px; line-height: 100px; letter-spacing: 2px; }
  .brand__descriptor { font-size: 19px; letter-spacing: 6.2px; margin-top: 18px; }

  .services {
    position: absolute; left: 96px; top: 263px;
    display: grid; grid-template-columns: 258px auto; row-gap: 2px;
    list-style: none;
  }
  .services li {
    display: flex; align-items: center; gap: 4px;
    color: var(--grey); font-size: 17.5px; line-height: 22px;
  }
  .services li svg { width: 12px; height: 16px; flex: none; }
</style>
</head>
<body>
  <svg width="0" height="0" style="position:absolute">
    <defs>
      <symbol id="bolt" viewBox="0 0 12 16"><path d="M7 0 L1 9 H5.5 L4 16 L11 6 H6.5 Z" fill="#dfa070"/></symbol>
    </defs>
  </svg>

  <section class="card card--front" aria-label="Business card front">
    <div class="holder">
      <p class="holder__name">DANIEL HARTLEY</p>
      <p class="holder__role">Managing Director</p>
    </div>

    <ul class="contact">
      <li class="contact__phone">
        <svg viewBox="0 0 16 16"><path d="M3.5 1.5 L6 4 L4.6 5.6 C5.5 7.6 8.4 10.5 10.4 11.4 L12 10 L14.5 12.5 L12.6 14.4 C8 14 2 8 1.6 3.4 Z" fill="none" stroke="#a3a3a3" stroke-width="1.5" stroke-linejoin="round"/></svg>
        0491736250
      </li>
      <li>
        <svg viewBox="0 0 16 16"><rect x="1" y="3.5" width="14" height="9.5" fill="#a3a3a3"/><path d="M1 3.5 L8 9 L15 3.5" fill="none" stroke="#070605" stroke-width="1.3"/></svg>
        info@ktlelectrical.com
      </li>
      <li>
        <svg viewBox="0 0 16 16" fill="none" stroke="#a3a3a3" stroke-width="1.2"><circle cx="8" cy="8" r="6.5"/><ellipse cx="8" cy="8" rx="3" ry="6.5"/><path d="M1.5 8 H14.5 M2.5 4.8 H13.5 M2.5 11.2 H13.5"/></svg>
        www.ktlelectrical.com
      </li>
    </ul>

    <address class="address">18 Carrington Street<br>Parramatta NSW 2150</address>

    <div class="feature-art" role="img" aria-label="Large outline illustration of an electrical plug with a lightning bolt"></div>
  </section>

  <section class="card card--back" aria-label="Business card back">
    <div class="brand">
      <p class="brand__name">K.T.L</p>
      <p class="brand__descriptor">ELECTRICAL SERVICES P/L</p>
    </div>

    <ul class="services">
      <li><svg><use href="#bolt"/></svg>Residential &amp; Commercial</li>
      <li><svg><use href="#bolt"/></svg>Maintenance</li>
      <li><svg><use href="#bolt"/></svg>PV &amp; Battery servicing</li>
      <li><svg><use href="#bolt"/></svg>EV Chargers</li>
    </ul>
  </section>
</body>
</html>
```